Business Card Design

We are a residential half way house for the addict ,the alcoholic and dual diagnosed in recovery.
i house both men and woman age 18+

Industry/Entity Type

Residential

```html
<!DOCTYPE html>
<html lang="en">
<head>
<meta charset="utf-8">
<title>Meadowlark Family Sober House – Business Card</title>
<link rel="stylesheet" href="https://fonts.googleapis.com/css2?family=Parisienne&family=Montserrat:wght@300;400;600&display=swap">
<style>
  :root {
    --bg: #e8e3da;
    --paper: #ffffff;
    --green: #8cc152;
    --green-dark: #4f9a3a;
    --red: #d9414a;
    --teal: #38b8c0;
    --yellow: #c9cc2e;
    --charcoal: #2f2d2c;
    --ink: #1d1d1d;
    --light-text: #ececec;
    --muted-text: #9a9896;
  }
  * { margin: 0; padding: 0; box-sizing: border-box; }
  html, body { width: 1200px; height: 800px; overflow: hidden; background: var(--bg); }
  .canvas { position: relative; width: 1200px; height: 800px; }

  .card {
    position: absolute; width: 580px; height: 330px; left: 310px;
    background: var(--paper); border-radius: 12px; overflow: hidden;
    box-shadow: 0 4px 14px rgba(0,0,0,.18);
  }
  .card--front { top: 45px; }
  .card--back { top: 425px; }

  .block { position: absolute; }
  .green { background: var(--green); }
  .red { background: var(--red); }
  .teal { background: var(--teal); }
  .yellow { background: var(--yellow); }

  .company-name {
    position: absolute; font-family: "Parisienne", cursive; font-weight: 400; color: var(--ink);
    text-align: center; line-height: 1.1; white-space: nowrap;
  }
  .card--front .company-name { left: 32px; right: 44px; top: 92px; font-size: 40px; }

  .address-ribbon { position: absolute; left: 185px; top: 200px; width: 230px; height: 44px; }
  .address-ribbon__text {
    position: absolute; left: 14px; right: 14px; top: 0; bottom: 0;
    background: var(--green); color: #fff;
    font-family: "Montserrat", sans-serif; font-weight: 600; font-size: 12px;
    line-height: 1.3; text-align: center; padding-top: 7px;
  }
  .address-rule { position: absolute; left: 32px; right: 44px; top: 244px; height: 7px; display: flex; }
  .address-rule span { flex: 1; }

  /* back */
  .card--back .white-panel { position: absolute; left: 30px; top: 0; width: 244px; height: 268px; background: var(--paper); }
  .card--back .company-name { left: 30px; width: 244px; top: 100px; font-size: 29px; }
  .dark-side { position: absolute; left: 300px; top: 0; right: 0; bottom: 0; background: var(--charcoal); }
  .holder { position: absolute; left: 348px; top: 82px; font-family: "Montserrat", sans-serif; }
  .holder__name { color: var(--light-text); font-size: 19px; letter-spacing: .5px; }
  .holder__name b { font-weight: 600; }
  .holder__name span { font-weight: 300; }
  .holder__role { color: var(--muted-text); font-size: 12.5px; font-weight: 300; margin-top: 2px; }

  .icon-cell { position: absolute; left: 300px; width: 30px; display: flex; align-items: center; justify-content: center; }
  .contact {
    position: absolute; left: 348px; color: var(--light-text);
    font-family: "Montserrat", sans-serif; font-weight: 300; font-size: 13px; line-height: 1.3;
  }
</style>
</head>
<body>
<main class="canvas">

  <section class="card card--front">
    <div class="block green" style="left:0;top:0;width:32px;height:110px"></div>
    <div class="block red" style="left:0;top:110px;width:32px;height:105px"></div>
    <div class="block yellow" style="left:0;top:215px;width:32px;height:115px"></div>
    <div class="block green" style="right:0;top:0;width:44px;height:95px"></div>
    <div class="block red" style="right:0;top:95px;width:44px;height:95px"></div>
    <div class="block yellow" style="right:0;top:190px;width:44px;height:140px"></div>

    <h1 class="company-name">Meadowlark Family<br>Sober House Inc.</h1>

    <div class="address-ribbon">
      <svg width="230" height="44" viewBox="0 0 230 44" style="position:absolute;left:0;top:0">
        <polygon points="0,44 14,0 14,44" fill="var(--green-dark)"/>
        <polygon points="230,44 216,0 216,44" fill="var(--green-dark)"/>
      </svg>
      <p class="address-ribbon__text">4820 Palmetto Ln. Lake Harbor,<br>Fla 33470</p>
    </div>
    <div class="address-rule">
      <span class="green"></span><span class="red"></span><span class="teal"></span><span class="yellow"></span><span class="green"></span>
    </div>
  </section>

  <section class="card card--back">
    <div class="block green" style="left:0;top:0;width:30px;height:60px"></div>
    <div class="block red" style="left:0;top:60px;width:30px;height:140px"></div>
    <div class="block green" style="left:0;top:200px;width:30px;height:130px"></div>

    <div class="block teal" style="left:30px;top:268px;width:100px;height:62px"></div>
    <div class="block green" style="left:130px;top:268px;width:100px;height:62px"></div>
    <div class="block yellow" style="left:230px;top:268px;width:44px;height:62px"></div>

    <div class="white-panel"></div>
    <h1 class="company-name">Meadowlark Family<br>Sober House Inc.</h1>

    <div class="block green" style="left:274px;top:0;width:26px;height:70px"></div>
    <div class="block red" style="left:274px;top:70px;width:26px;height:180px"></div>
    <div class="block yellow" style="left:274px;top:250px;width:26px;height:80px"></div>

    <div class="dark-side"></div>

    <div class="holder">
      <p class="holder__name"><b>RENATA</b> <span>MORALES</span></p>
      <p class="holder__role">Owner - 15 yrs. in recovery</p>
    </div>

    <div class="icon-cell teal" style="top:130px;height:42px">
      <svg width="12" height="18" viewBox="0 0 12 18" aria-hidden="true"><rect x="1" y="1" width="10" height="16" rx="2" fill="none" stroke="#fff" stroke-width="1.6"/><rect x="3" y="3.5" width="6" height="8" fill="#fff"/></svg>
    </div>
    <div class="icon-cell red" style="top:172px;height:62px">
      <svg width="18" height="14" viewBox="0 0 18 14" aria-hidden="true"><rect x="3" y="1" width="12" height="8" fill="none" stroke="#fff" stroke-width="1.6"/><rect x="0" y="11" width="18" height="2" fill="#fff"/></svg>
    </div>
    <div class="icon-cell green" style="top:234px;height:36px">
      <svg width="16" height="12" viewBox="0 0 16 12" aria-hidden="true"><rect x="0" y="0" width="16" height="12" fill="#fff"/><polyline points="0,0 8,7 16,0" fill="none" stroke="var(--green)" stroke-width="1.4"/></svg>
    </div>

    <p class="contact" style="top:134px">(555) 014-0187<br>(555) 014-0188</p>
    <p class="contact" style="top:194px">Fax (555) 014-0192</p>
    <p class="contact" style="top:244px">renatamorales@mailbox.com</p>
  </section>

</main>
</body>
</html>
```